Harlow Ridge Partners Business Cards

Design Business cards in a format where I can change the information and utilize a third party buisness card printing company

Contact Information for Business Card

Want Logo and Name on Back. Looking for Spot UV style shine on Logo. Probably Black background. Want smaller logo on front with contact details. Like rounded edges or something else interesting.

Requirements
Must have
• Strong masculine look.

```html
<!DOCTYPE html>
<html lang="en">
<head>
<meta charset="utf-8">
<title>Harlow Ridge Partners – Business Cards</title>
<link rel="stylesheet" href="https://fonts.googleapis.com/css2?family=Roboto:wght@400;500&family=Roboto+Condensed:wght@500&display=swap">
<style>
  :root {
    --backdrop: #2b2b2c;
    --card: #1b1b1c;
    --band: #6a6a6d;
    --name-ink: #1c1c1d;
    --text-light: #d8d8d8;
    --brand-grey: #7a7a7c;
    --brand-silver: #d4d4d6;
    --icon: #bdbdbd;
  }
  * { margin: 0; padding: 0; box-sizing: border-box; }
  html, body { width: 1200px; height: 960px; overflow: hidden; }
  body {
    position: relative;
    background: var(--backdrop);
    font-family: "Roboto", Arial, sans-serif;
    color: var(--text-light);
  }
  .card {
    position: absolute;
    left: 323px;
    width: 597px;
    height: 342px;
    background: var(--card);
    border-radius: 14px;
    overflow: hidden;
  }
  .card--front { top: 110px; }
  .card--back { top: 494px; }

  .name-band {
    position: absolute;
    left: 0; top: 48px;
    width: 400px; height: 52px;
    background: var(--band);
    padding: 6px 0 0 30px;
    color: var(--name-ink);
  }
  .name-band__name {
    font-family: "Roboto Condensed", "Arial Narrow", sans-serif;
    font-weight: 500;
    font-size: 23px;
    line-height: 26px;
  }
  .name-band__title { font-size: 14px; line-height: 16px; }

  .brand-name {
    position: absolute;
    font-family: "Roboto", Arial, sans-serif;
    font-weight: 500;
    letter-spacing: 1px;
    display: flex;
    align-items: center;
    gap: 10px;
    white-space: nowrap;
  }
  .brand-name__square { display: block; width: 14px; height: 14px; }
  .card--front .brand-name {
    right: 34px; top: 146px;
    font-size: 20px;
    color: var(--brand-grey);
  }
  .card--front .brand-name__square { background: var(--brand-grey); }
  .card--back .brand-name {
    left: 0; right: 0; top: 152px;
    justify-content: center;
    font-size: 30px;
    color: var(--brand-silver);
  }
  .card--back .brand-name__square { width: 20px; height: 20px; background: var(--brand-silver); }

  .contact-list {
    position: absolute;
    left: 31px; top: 243px;
    list-style: none;
    font-size: 14px;
    line-height: 19.3px;
  }
  .contact-list li { display: flex; align-items: center; gap: 8px; }
  .contact-list svg { width: 14px; height: 14px; fill: var(--icon); flex: none; }

  .address {
    position: absolute;
    right: 31px; top: 264px;
    text-align: right;
    font-size: 14px;
    line-height: 18.5px;
  }
  .address__web { letter-spacing: 2.2px; }
</style>
</head>
<body>

<section class="card card--front">
  <div class="name-band">
    <div class="name-band__name">DANIEL REEVE</div>
    <div class="name-band__title">CEO/Founder</div>
  </div>

  <div class="brand-name"><span class="brand-name__square"></span>Harlow Ridge Partners</div>

  <ul class="contact-list">
    <li>
      <svg viewBox="0 0 24 24"><path d="M6.6 10.8a15.1 15.1 0 0 0 6.6 6.6l2.2-2.2c.3-.3.7-.4 1-.2 1.1.4 2.3.6 3.6.6.6 0 1 .4 1 1V20c0 .6-.4 1-1 1A17 17 0 0 1 3 4c0-.6.4-1 1-1h3.5c.6 0 1 .4 1 1 0 1.3.2 2.5.6 3.6.1.3 0 .7-.2 1z"/></svg>
      614 220 7391
    </li>
    <li>
      <svg viewBox="0 0 24 24"><path d="M7 1h10a2 2 0 0 1 2 2v18a2 2 0 0 1-2 2H7a2 2 0 0 1-2-2V3a2 2 0 0 1 2-2zm0 3v15h10V4z"/></svg>
      614 220 7392
    </li>
    <li>
      <svg viewBox="0 0 24 24"><path d="M6 2h12v5H6zM3 8h18a2 2 0 0 1 2 2v7h-4v5H5v-5H1v-7a2 2 0 0 1 2-2zm4 8v4h10v-4z"/></svg>
      614 220 7393
    </li>
    <li>
      <svg viewBox="0 0 24 24"><path d="M2 5h20v14H2zm2 2v.5l8 5 8-5V7z"/></svg>
      daniel@harlowridge.com
    </li>
  </ul>

  <address class="address" style="font-style:normal">
    <div>412 Juniper Court</div>
    <div>Fairbanks, Alaska 99701</div>
    <div class="address__web">www.harlowridge.com</div>
  </address>
</section>

<section class="card card--back">
  <div class="brand-name"><span class="brand-name__square"></span>Harlow Ridge Partners</div>
</section>

</body>
</html>
```